Birthday Party Invitation for Jasper's 18th Birthday Party

Our eldest son Jasper is turning 18 and we are having a party at home to celebrate the occasion. This project is about creating an invitation that will go to our friends and family. We like things to be nicely designed so posting it to pixel harbor seemed to be the way to go.
The invitation needs to be able to be printed onto an A4 piece of paper. We have access to a color copier so it can be nice and bright.

We want an invitation that conveys a sense of occasion and looks as though we have put time and effort into having a great night to celebrate his 18th.
I have included some photo's of Jasper. They can go onto the invitation as is or they can be given some treatment to form a theme when on the invitiation. I'll leave the treatment of the photo's to the individual designer.

Target Market(s)

Friends and Family

Font styles to use
Sans Serif

Colors

Designer to choose colors to be used in the design.

Requirements
Must have
• The invitation must have the time, date and location of the party.
• Details:
• Saturday 29th of July 2017 7.00pm
• 41 Brackmere Lane, Fenwood
• Food and Drinks provided It must be bright and colourful and convey a sense of excitement.
Nice to have
• Inclusion of the photo's that I have uploaded.
Should not have
• any boring bits

```html
<!DOCTYPE html>
<html lang="en">
<head>
<meta charset="utf-8">
<title>Jasper's Eighteenth Birthday</title>
<link rel="stylesheet" href="https://fonts.googleapis.com/css2?family=Josefin+Sans:wght@400&family=Allura&family=Playfair+Display:wght@400&display=swap">
<style>
  :root {
    --bg: #2b2b2b;
    --ink: #ececec;
    --title: #f2f2f2;
    --glow: rgba(255, 255, 255, 0.45);
    --polaroid: #f4f4f2;
    --tape: rgba(214, 208, 196, 0.85);
    --star-yellow: #f7e11b;
    --star-blue: #2f9fe0;
    --star-pink: #ec1f6a;
    --star-green: #8cc63f;
    --star-teal: #13a89e;
    --star-orange: #f7931e;
  }
  * { margin: 0; padding: 0; box-sizing: border-box; }
  html, body { width: 846px; height: 1200px; overflow: hidden; background: var(--bg); }
  .invitation { position: relative; width: 846px; height: 1200px; background: var(--bg); overflow: hidden; }
  .age-numeral { position: absolute; left: 0; top: 0; width: 846px; height: 760px; }
  .age-numeral text { font-family: "Playfair Display", serif; font-weight: 400; }
  .event-title { position: absolute; left: 0; top: 770px; width: 846px; height: 140px; }
  .event-title text {
    font-family: "Allura", cursive;
    fill: var(--title);
    filter: drop-shadow(0 0 5px var(--glow));
  }
  .event-details {
    position: absolute; left: 228px; top: 964px; width: 384px; z-index: 2;
    text-align: center; list-style: none;
    font-family: "Josefin Sans", sans-serif; font-size: 18px;
    letter-spacing: 2px; text-transform: uppercase; color: var(--ink);
    line-height: 32px; white-space: nowrap;
  }
  .polaroid {
    position: absolute; z-index: 1; background: var(--polaroid);
    box-shadow: 0 4px 10px rgba(0, 0, 0, 0.45);
    padding: 12px 12px 38px;
  }
  .polaroid-left { left: 34px; top: 945px; width: 176px; height: 190px; transform: rotate(-12deg); }
  .polaroid-right { left: 628px; top: 952px; width: 176px; height: 200px; transform: rotate(11deg); }
  .photo { width: 100%; height: 100%; }
  .photo-waterpolo { background: linear-gradient(160deg, #cfd6dc 0%, #9fb0bd 55%, #d9c2b0 100%); }
  .photo-harbour { background: linear-gradient(180deg, #b9cbd8 0%, #8b9aa6 45%, #4a3f3c 100%); }
  .tape { position: absolute; width: 54px; height: 20px; background: var(--tape); }
  .tape-top-left { left: -22px; top: 8px; transform: rotate(-45deg); }
  .tape-bottom-right { right: -22px; bottom: 12px; transform: rotate(-45deg); }
  .tape-top-right { right: -22px; top: 8px; transform: rotate(45deg); }
  .tape-bottom-left { left: -22px; bottom: 12px; transform: rotate(45deg); }
</style>
</head>
<body>
<main class="invitation">
  <svg class="age-numeral" viewBox="0 0 846 760" aria-label="18">
    <defs>
      <linearGradient id="starfield" x1="0" y1="0" x2="1" y2="1">
        <stop offset="0" stop-color="var(--star-teal)"/>
        <stop offset="0.18" stop-color="var(--star-yellow)"/>
        <stop offset="0.34" stop-color="var(--star-blue)"/>
        <stop offset="0.5" stop-color="var(--star-pink)"/>
        <stop offset="0.66" stop-color="var(--star-green)"/>
        <stop offset="0.82" stop-color="var(--star-orange)"/>
        <stop offset="1" stop-color="var(--star-blue)"/>
      </linearGradient>
    </defs>
    <text x="50" y="712" font-size="790" textLength="740" lengthAdjust="spacingAndGlyphs" fill="url(#starfield)">18</text>
  </svg>

  <svg class="event-title" viewBox="0 0 846 140">
    <text x="423" y="100" font-size="110" text-anchor="middle" textLength="680" lengthAdjust="spacingAndGlyphs">Jasper's Eighteenth Birthday</text>
  </svg>

  <ul class="event-details">
    <li>Saturday 29th of July - 7.00pm</li>
    <li>41 Brackmere Lane, Fenwood</li>
    <li>Food and drinks provided</li>
  </ul>

  <figure class="polaroid polaroid-left">
    <div class="photo photo-waterpolo" role="img" aria-label="Photo of Jasper as a boy playing water polo, holding the ball up in the pool"></div>
    <span class="tape tape-top-left"></span>
    <span class="tape tape-bottom-right"></span>
  </figure>

  <figure class="polaroid polaroid-right">
    <div class="photo photo-harbour" role="img" aria-label="Photo of Jasper smiling by the harbour with the bridge behind him"></div>
    <span class="tape tape-top-right"></span>
    <span class="tape tape-bottom-left"></span>
  </figure>
</main>
</body>
</html>
```